Medical Aesthetics business cards

Looking for a business card for my new medical aesthetics business. I am a nurse practitioner and will be administering dravine , fillers as well as providing other services

```html
<!DOCTYPE html>
<html lang="en">
<head>
<meta charset="UTF-8">
<title>Nurse Practitioner Business Card</title>
<link href="https://fonts.googleapis.com/css2?family=Open+Sans:wght@400;600&display=swap" rel="stylesheet">
<style>
  :root {
    --page-bg: #e9e6e1;
    --card-dark: #0a1628;
    --card-mid: #16243a;
    --card-light: #2b3b52;
    --accent-blue: #1ea7e8;
    --accent-deep: #1a5f8e;
    --text-light: #ffffff;
  }
  html, body {
    margin: 0;
    padding: 0;
    width: 1200px;
    height: 900px;
    overflow: hidden;
    background: var(--page-bg);
  }
  .canvas {
    position: relative;
    width: 1200px;
    height: 900px;
    display: flex;
    align-items: center;
    justify-content: center;
  }
  .business-card {
    position: relative;
    width: 840px;
    height: 480px;
    background: linear-gradient(100deg, var(--card-dark) 0%, var(--card-mid) 55%, var(--card-light) 100%);
    box-shadow: 0 10px 30px rgba(0, 0, 0, 0.25);
    overflow: hidden;
  }
  .corner-accent {
    position: absolute;
    display: block;
  }
  .corner-accent--top-left {
    top: 0;
    left: 0;
    width: 420px;
    height: 140px;
  }
  .corner-accent--bottom-right {
    right: 0;
    bottom: 0;
    width: 420px;
    height: 190px;
  }
  .job-title {
    position: absolute;
    left: 0;
    right: 0;
    top: 50%;
    transform: translateY(-50%);
    margin: 0;
    text-align: center;
    font-family: 'Open Sans', sans-serif;
    font-weight: 400;
    font-size: 42px;
    letter-spacing: 1px;
    color: var(--text-light);
  }
</style>
</head>
<body>
<main class="canvas">
  <section class="business-card">
    <svg class="corner-accent corner-accent--top-left" viewBox="0 0 420 140" role="img" aria-label="Scattered blue square pattern accent in top-left corner">
      <defs>
        <radialGradient id="accentTopLeft" cx="0" cy="0" r="1" gradientUnits="objectBoundingBox">
          <stop offset="0" stop-color="var(--accent-blue)" stop-opacity="0.75"/>
          <stop offset="0.45" stop-color="var(--accent-deep)" stop-opacity="0.35"/>
          <stop offset="1" stop-color="var(--accent-deep)" stop-opacity="0"/>
        </radialGradient>
      </defs>
      <rect width="420" height="140" fill="url(#accentTopLeft)"/>
    </svg>

    <h1 class="job-title">NURSE PRACTITIONER</h1>

    <svg class="corner-accent corner-accent--bottom-right" viewBox="0 0 420 190" role="img" aria-label="Scattered blue square pattern accent in bottom-right corner">
      <defs>
        <radialGradient id="accentBottomRight" cx="1" cy="1" r="1" gradientUnits="objectBoundingBox">
          <stop offset="0" stop-color="var(--accent-blue)" stop-opacity="0.75"/>
          <stop offset="0.45" stop-color="var(--accent-deep)" stop-opacity="0.35"/>
          <stop offset="1" stop-color="var(--accent-deep)" stop-opacity="0"/>
        </radialGradient>
      </defs>
      <rect width="420" height="190" fill="url(#accentBottomRight)"/>
    </svg>
  </section>
</main>
</body>
</html>
```